Verdant Press Bottle Label

I am looking to design a bottle for my company verdant press. I have attached the Logo. I would like a label that would include the following.
Name of Juice - K7
Company Logo - attached
Ingredients - Kale,Broccoli, Spinach, Apple, and Cucumber
Health Benefits - K7 is a combination of fruits and vegetables specifically designed to ouwefo wjnwj ekw ckjbewj jw cejnvej (The exact verbage will be added later its the design and look that matters right now)
The bottle it needs to fit on is 6 inches tall and 2 1/4 square (It's the middle bottle in the picture attached.
I am looking for a label that matches the logo.
Thanks.

```html
<!DOCTYPE html>
<html lang="en">
<head>
<meta charset="utf-8">
<title>Verdant Press – K7 Bottle Label</title>
<link href="https://fonts.googleapis.com/css2?family=Arimo:wght@400;700&family=Saira+Stencil+One&display=swap" rel="stylesheet">
<style>
  :root {
    --page: #ffffff;
    --orange: #f7941d;
    --orange-deep: #f08a1c;
    --orange-light: #fbb040;
    --cream: #fff6ea;
    --green: #17893b;
    --ink: #1c1c1c;
    --rule: #6d6d6d;
    --produce-red: #c7332e;
    --produce-green: #7cb53f;
  }
  * { margin: 0; padding: 0; box-sizing: border-box; }
  html, body {
    width: 1200px; height: 1000px; overflow: hidden;
    background: var(--page);
    font-family: "Arimo", Arial, sans-serif;
    color: var(--ink);
  }
  .label {
    position: absolute; left: 23px; top: 225px;
    width: 1157px; height: 560px; overflow: hidden;
    background: radial-gradient(ellipse 420px 330px at 577px 230px,
      #ffffff 0%, var(--cream) 30%, #fcd3a0 60%, var(--orange) 100%);
  }
  .label-decor { position: absolute; inset: 0; }
  .stencil-mark {
    font-family: "Saira Stencil One", "Arimo", sans-serif;
    fill: none; stroke-width: 2;
  }
  .ingredients { position: absolute; left: 12px; top: 8px; font-size: 16px; line-height: 20px; }
  .ingredients h2 { font-size: 17px; font-weight: 700; }
  .brand { position: absolute; left: 267px; top: 180px; width: 620px; }
  .brand-name {
    margin-left: 198px;
    font-size: 64px; font-weight: 700; color: var(--green);
    letter-spacing: -1px; line-height: 70px;
  }
  .brand-rule { height: 1px; background: var(--rule); margin-top: 6px; }
  .brand-tagline {
    margin-left: 198px; margin-top: 4px;
    font-size: 15px; font-weight: 700; letter-spacing: 0.2px;
  }
  .produce {
    position: absolute; left: 427px; top: 300px; width: 420px; height: 180px;
    border-radius: 90px;
    background: linear-gradient(90deg, var(--produce-red) 0%, #5f9a35 35%, var(--produce-green) 65%, #a6cf5a 100%);
    opacity: 0.85;
  }
  .benefits {
    position: absolute; left: 942px; top: 365px; width: 205px;
    text-align: center; font-size: 15px; line-height: 19px;
  }
  .benefits h3 { font-size: 15px; font-weight: 700; line-height: 19px; }
  .benefits .fill-line { letter-spacing: 0.5px; overflow: hidden; white-space: nowrap; }
</style>
</head>
<body>
  <section class="label">
    <svg class="label-decor" width="1157" height="560" viewBox="0 0 1157 560">
      <g class="top-right-rings" fill="none" stroke="#f9a545" opacity="0.55">
        <circle cx="1090" cy="80" r="260" stroke-width="40"/>
        <circle cx="1090" cy="80" r="170" stroke-width="30"/>
        <circle cx="1090" cy="80" r="90" stroke-width="20"/>
      </g>
      <path class="rising-arrow" d="M10 210 L90 125 L170 210 L130 210 L130 560 L50 560 L50 210 Z" fill="#fbb257" opacity="0.45"/>
      <g class="bottom-left-rings">
        <circle cx="110" cy="480" r="240" fill="#fbb040"/>
        <circle cx="110" cy="480" r="225" fill="#f7a02e"/>
        <circle cx="110" cy="480" r="195" fill="#f6892a"/>
        <circle cx="110" cy="480" r="178" fill="#f9a53c"/>
        <circle cx="110" cy="480" r="150" fill="#f28128"/>
        <circle cx="110" cy="480" r="132" fill="#f9a33a"/>
        <circle cx="110" cy="480" r="100" fill="#f5902a"/>
        <circle cx="110" cy="480" r="75" fill="#fbb040"/>
      </g>
      <text class="stencil-mark" x="10" y="545" font-size="130" stroke="#fde3bf">K7</text>
      <text class="stencil-mark" x="1025" y="115" font-size="110" stroke="#fbbd6e">K7</text>
    </svg>

    <div class="ingredients">
      <h2>Ingredients:</h2>
      <p>Kale, Broccoli, Spinach<br>Apple, and Cucumber.</p>
    </div>

    <div class="brand">
      <div class="brand-name">Verdant Press</div>
      <div class="brand-rule"></div>
      <div class="brand-tagline">FRESH JUICE DELIVERED DIRECTLY TO YOUR DOOR</div>
    </div>

    <div class="produce" role="img" aria-label="Photo of fresh broccoli, red apples, spinach leaves, sliced cucumber and a green apple"></div>

    <div class="benefits">
      <h3>GIVE YOUR BODY<br>WHAT IT DESERVES</h3>
      <p>K7 is a combination of fruits and vegetables specifically designed to..........................</p>
      <p class="fill-line">..............................................</p>
      <p class="fill-line">..............................................</p>
      <p class="fill-line">..............................................</p>
    </div>
  </section>
</body>
</html>
```